Business Card Design Project

I am a Chiropractor that is looking for a new business card.  Our logo was slightly changed lately, therefore need a new, more professional look.
We are a modern, non-stuffy chiropractic office.  Want a contemporary look that will let people know this is not your typical doctors office.  Our logo is red, and contains the name of our business: realign.  The u in the logo is green, stressing the most important part of our business: "u"

Target Market(s)
moderate to upper income bracket, family friendly
www.realignspine-example.com
Gordon Pell
Family Chiropractor
314 Hollis Rd
Fernvale, ND 58999
555.010.0147 phone
555.010.0148 fax
Industry/Entity Type
Business
Requirements
Must have
- www.realignspine-example.com
Gordon Pell
Family Chiropractor
314 Hollis Rd
Fernvale, ND 58999
555.010.0147 phone
555.010.0148 fax

```html
<!DOCTYPE html>
<html lang="en">
<head>
<meta charset="utf-8">
<title>realign – Business Card</title>
<link rel="stylesheet" href="https://fonts.googleapis.com/css2?family=PT+Sans:wght@400;700&display=swap">
<style>
  :root {
    --backdrop: #e4e4e4;
    --card: #ffffff;
    --brand-red: #e8413a;
    --name-red: #b34a42;
    --brand-green: #6db84a;
    --ink: #1e1e1e;
  }
  * { margin: 0; padding: 0; box-sizing: border-box; }
  html, body {
    width: 954px;
    height: 1200px;
    overflow: hidden;
    background: var(--backdrop);
    font-family: "PT Sans", sans-serif;
    color: var(--ink);
  }
  .card {
    position: absolute;
    left: 85px;
    width: 795px;
    height: 454px;
    background: var(--card);
    border-radius: 28px;
  }
  .card--front { top: 68px; }
  .card--back { top: 645px; }

  .brand {
    position: absolute;
    top: 90px;
    left: 0;
    width: 100%;
    text-align: center;
    font-size: 92px;
    font-weight: 400;
    line-height: 1;
    letter-spacing: 1px;
    color: var(--brand-red);
  }
  .identity {
    position: absolute;
    top: 302px;
    width: 100%;
    text-align: center;
    font-size: 19px;
    white-space: nowrap;
  }
  .identity__name,
  .identity__dash {
    font-size: 27px;
    font-weight: 700;
    color: var(--name-red);
  }
  .contact {
    position: absolute;
    width: 100%;
    text-align: center;
    font-size: 21px;
    white-space: nowrap;
  }
  .contact--phones { top: 366px; }
  .contact--web { top: 404px; font-size: 20px; }
  .contact__label { font-weight: 700; }
  .contact__url { font-size: 23px; }
  .contact__sep { margin: 0 12px; }

  .back-mark {
    position: absolute;
    top: 118px;
    left: 0;
    width: 100%;
    text-align: center;
    font-size: 140px;
    font-weight: 400;
    line-height: 1;
    color: var(--brand-green);
  }
  .back-url {
    position: absolute;
    top: 377px;
    width: 100%;
    text-align: center;
    font-size: 25px;
  }
</style>
</head>
<body>
  <section class="card card--front">
    <div class="brand">realign</div>
    <p class="identity">
      <span class="identity__name">Gordon Pell</span>
      <span class="identity__dash">-</span> Family Chiropractor
    </p>
    <p class="contact contact--phones">
      <span class="contact__label">p</span> : 555.010.0147<span class="contact__sep">|</span><span class="contact__label">f</span> : 555.010.0148
    </p>
    <p class="contact contact--web">
      <span class="contact__url"><span class="contact__label">w</span> : www.realignspine-example.com</span><span class="contact__sep">|</span>314 Hollis Rd, Fernvale, ND 58999
    </p>
  </section>

  <section class="card card--back">
    <div class="back-mark">realign</div>
    <p class="back-url">www.realignspine-example.com</p>
  </section>
</body>
</html>
```